Flyer for American Indian Elders on Dementia Warning Signs

We need a flyer designed for older adults who are American Indian or Alaska Native (in the U.S.).

Ideally, the flyer should complement the colors of our logos. The project logo and our organization logo are attached to the brief.

When people see the flyer we want them to feel that it represents their culture, is warm, and professional but relatable to older adults and people who have limited incomes.

I have attached an earlier draft of the document we designed ourselves BUT we want different and better.

It is for older adults who have trouble reading so:
1. you must use a font that is 11.5 points or larger
2. Do not put text over complex pictures or use shading with words
3. You can use a serif font for the heading, but should use san serif for the body text
4. There should be good contrast between the font color and background

Please do not use any images that include a head dress or pictures of American Indian people or things that are very traditional or "token" imagery.

We need to save a small space under the call out box/ somewhere on the flyer for other people to add their logo once they download.

Let us know if you have questions or need additional information.

Target Market(s)

Older American Indian people

Font styles to use
Serif
Sans Serif

Requirements
Must have
• Easy to read for older adults
Should not have
• indian headdress

```html
<!DOCTYPE html>
<html lang="en">
<head>
<meta charset="UTF-8">
<title>10 Signs of Thinking or Memory Changes – Flyer</title>
<link href="https://fonts.googleapis.com/css2?family=Playfair+Display:wght@400;700&family=Raleway:wght@400;500;600;700&display=swap" rel="stylesheet">
<style>
  :root{
    --teal:#4fa8b0;
    --teal-dark:#3e8f97;
    --rose:#b0605a;
    --rose-text:#a8453f;
    --sky:#c2f5fb;
    --blush:#fbd7d7;
    --paper:#f2f2f0;
    --ink:#2f2f2f;
    --stage:#b3b3b3;
  }
  *{box-sizing:border-box;margin:0;padding:0}
  html,body{width:1009px;height:1200px;overflow:hidden;background:var(--stage)}
  .flyer{
    position:absolute;left:80px;top:0;width:848px;height:1200px;
    background:var(--paper);font-family:"Raleway",sans-serif;color:var(--ink);
    letter-spacing:-0.3px;
  }
  .art{position:absolute;border-radius:8px}
  .art-dreamcatcher{left:14px;top:34px;width:136px;height:172px;z-index:2;
    background:radial-gradient(circle at 50% 35%,#d9a86a 0,#b98a55 35%,rgba(120,120,120,.35) 70%,transparent 72%);}
  .art-feather-right{left:772px;top:410px;width:64px;height:135px;
    background:linear-gradient(160deg,#5aa6a6,#2f6f73);border-radius:50% 50% 50% 50%/60% 60% 40% 40%;transform:rotate(-18deg)}
  .art-feather-left{left:4px;top:920px;width:70px;height:182px;z-index:2;
    background:linear-gradient(200deg,#5aa6a6,#2f6f73);border-radius:50% 50% 50% 50%/60% 60% 40% 40%;transform:rotate(18deg)}
  .art-tipi{left:712px;top:998px;width:126px;height:150px;z-index:2;
    background:linear-gradient(180deg,#d9c79b,#a88a4e);clip-path:polygon(50% 0,100% 100%,0 100%);border-radius:0}

  .brand-row{position:absolute;top:28px;left:150px;width:560px;height:62px;display:flex;align-items:center;gap:18px}
  .brand{display:flex;align-items:center;gap:8px;font-weight:700;line-height:1.05}
  .brand .dot{width:46px;height:46px;border-radius:50%;background:var(--teal);flex:none}
  .brand .name{font-size:14px;color:var(--teal-dark)}
  .brand .name small{display:block;font-size:9px;color:var(--rose-text);font-weight:600}
  .brand-two .dot{background:var(--rose);border-radius:4px}
  .brand-two .name{color:var(--rose-text);font-size:15px}
  .brand-divider{width:1px;height:56px;background:var(--ink)}

  .title-band{position:absolute;left:52px;top:104px;width:744px;height:88px;border-radius:8px;
    background:linear-gradient(90deg,var(--teal) 0,var(--teal) 35%,var(--rose) 75%);
    display:flex;align-items:center;justify-content:center;text-align:center}
  .title-band h1{font-family:"Playfair Display",serif;font-weight:400;color:#fff;font-size:34px;line-height:1.1}

  .intro{position:absolute;left:52px;top:210px;width:744px;font-size:15.5px;line-height:1.45;text-align:center}
  .intro p{margin-bottom:10px}
  .intro strong{font-weight:700}

  .signs{position:absolute;top:334px;width:365px;height:553px;border-radius:10px;padding:18px 22px 0 26px}
  .signs-left{left:52px;background:var(--sky)}
  .signs-right{left:430px;background:var(--blush);padding-left:18px}
  .sign{margin-bottom:18px}
  .sign h2{font-family:"Playfair Display",serif;font-weight:700;font-size:17px;line-height:1.15;color:#404040;margin-bottom:5px;letter-spacing:-0.6px}
  .sign h2 span{font-family:"Raleway",sans-serif;font-weight:500;font-size:14.5px;letter-spacing:-0.5px}
  .sign p,.sign li{font-size:15.5px;line-height:1.28;letter-spacing:-0.55px}
  .sign p{padding-left:12px}
  .sign ul{list-style:none}
  .sign li{padding-left:12px;position:relative}
  .sign li::before{content:"›";position:absolute;left:0;top:-1px}

  .facts{position:absolute;left:52px;top:900px;width:744px;height:138px;background:var(--teal);border-radius:8px;
    display:grid;grid-template-columns:1fr 1fr;column-gap:20px;padding:10px 30px 0 30px;color:#fff}
  .facts ul{list-style:none}
  .facts li{font-size:16px;line-height:1.42;padding-left:12px;position:relative;margin-bottom:10px}
  .facts li::before{content:"›";position:absolute;left:0}
  .facts-right{padding-right:14px}

  .logo-slot{position:absolute;left:0;width:848px;top:1074px;text-align:center;color:var(--rose-text);font-size:19px;font-weight:500}

  .footer{position:absolute;left:0;bottom:0;width:848px;height:67px;background:var(--rose);
    display:flex;align-items:center;justify-content:center;color:#fff;font-weight:700;font-size:17.5px}
</style>
</head>
<body>
<main class="flyer">
  <div class="art art-dreamcatcher" role="img" aria-label="Dream catcher with hanging feathers"></div>

  <header class="brand-row">
    <div class="brand brand-one"><span class="dot"></span><span class="name">NATIVE ELDERS<br>BRAIN WELLNESS<small>CENTER</small></span></div>
    <span class="brand-divider"></span>
    <div class="brand brand-two"><span class="dot"></span><span class="name">CIRCLE OF ELDERS<br>AGING ALLIANCE</span></div>
  </header>

  <div class="title-band"><h1>10 Signs of Thinking or Memory<br>Changes that Might be Dementia</h1></div>

  <section class="intro">
    <p>As we get older, we may slow down a bit. This is a normal part of aging. Changes in memory or thinking that make it harder to get through the day, are not a normal part of aging. These may be early signs of dementia.</p>
    <p>Because American Indian and Alaska Native people have a high risk of dementia, it is mportant to know the warning signs. <strong>Do you have any of these 10 signs? If so, talk to your doctor.</strong></p>
  </section>

  <section class="signs signs-left">
    <div class="sign"><h2>1. Memory loss that affects your daily life</h2>
      <ul><li>Repeat yourself</li><li>Rely more often on lists or sticky notes to remember things</li></ul></div>
    <div class="sign"><h2>2. Trouble planning or solving problems</h2>
      <ul><li>Paying bills</li><li>Cooking recipes you have used for years</li></ul></div>
    <div class="sign"><h2>3. Trouble with how your eyesight &amp; thinking work together or gets worse</h2>
      <p>Tripping, falls, or problems with your balance<br>Spilling or dropping things more</p></div>
    <div class="sign"><h2>4. New trouble talking or writing</h2>
      <p>You have a hard time finding the words you want to say. For example, you may say “that thing on your wrist that tells time” instead of “watch.”</p></div>
    <div class="sign"><h2>5. Notice changes in mood or personality</h2>
      <ul><li>Easily mad or sad in everyday situations</li><li>More fearful (scared) or suspicious (not trusting)</li></ul></div>
  </section>

  <section class="signs signs-right">
    <div class="sign"><h2>6. Lose &amp; cannot find things <span>For Example you:</span></h2>
      <ul><li>Can’t find the coffee pot you use everyday</li><li>Might put your car keys in the freezer</li></ul></div>
    <div class="sign"><h2>7. Daily tasks are getting harder <span>including:</span></h2>
      <ul><li>Driving</li><li>Making a grocery list or going shopping</li></ul></div>
    <div class="sign"><h2>8. Pull away from friends &amp; family because it is harder to keep up</h2>
      <p>You may not want to do things you used to enjoy like sports, church, music or sex</p></div>
    <div class="sign"><h2>9. Act different &amp; make poor choices <span>This may make you more likely to:</span></h2>
      <ul><li>Spend money you do not have or be a scam victim</li><li>Stop washing up regularly or pay less attention to how you look</li><li>Forget to take care of your pet</li></ul></div>
    <div class="sign"><h2>10. Get confused about the time, date, or where you are</h2></div>
  </section>
  <div class="art art-feather-right" role="img" aria-label="Teal feather"></div>

  <section class="facts">
    <ul class="facts-left"><li>American Indian and Alaska Native people have a high risk of dementia.</li>
      <li>Big changes in memory or thinking that make it hard to get through the day are not a normal part of aging.</li></ul>
    <ul class="facts-right"><li>Early dementia diagnosis gives you a chance to get care and plan your future</li>
      <li>People with one or more of these 10 signs should talk to their doctor to find the cause. It is not always dementia.</li></ul>
  </section>
  <div class="art art-feather-left" role="img" aria-label="Teal feather"></div>
  <div class="art art-tipi" role="img" aria-label="Tipi illustration"></div>

  <p class="logo-slot">LOGO GOES HERE</p>

  <footer class="footer">To learn more visit: www.eldermindcircle.org&nbsp;|&nbsp; www.healthyagingnet.org</footer>
</main>
</body>
</html>
```